The Quiet Pantry Method: Reshape Your Habits Around Meals in Only 30 Days

I want a book cover for a paperback non-fiction book 30 day challenge to transform you relationship with your food, diet and lifestyle for longterm health and vitality. I would like to incorporate two photos on the front cover, one of a Greek salad and one of me the author. I have uploaded the four photos. Use which of each pair you think best. Because of my name, I want the photo on the cover. Otherwise folks assume Marla is a guy.
I am looking at best selling health books and they seem to be on the lighter side color-wise, with horizontal design. Green and orange seem to work most often, though my logo is a bluish turquoise (https://marlavoskin.com). I would imagine a light background, clear simple fonts. Looking forward to your designs!

Target Market(s)

Women around 35-40 confused by conflicting nutrition information but dedicated to better health haelthy

Industry/Entity Type

nutrition and wellness

Font styles to use
Serif

Colors
00AB8E
00BBA5
67D7C9
C6EFE9
E9F9F6
F0912C
F2A743
F7CA91
FBE8D2
FDF5EE
EE7325
F08F49
F5BC92
FAE3D3
FDF4ED

Requirements
Must have
• Clear simple look with room for an endorsement
Nice to have
• Hints of natural scenes and happy places
Should not have
• Dark or ominous feel

```html
<!DOCTYPE html>
<html lang="en">
<head>
<meta charset="utf-8">
<title>The Quiet Pantry Method — Marla Voskin</title>
<link rel="stylesheet" href="https://fonts.googleapis.com/css2?family=Oswald:wght@500;600;700&display=swap">
<style>
  :root {
    --page-bg: #ececec;
    --cover-bg: #d0e3ec;
    --band: #6fafcd;
    --subtitle: #6aabcb;
    --title: #0a0a0a;
    --author-text: #ffffff;
    --plate-rim: #ffffff;
    --salad-green: #4f9a33;
    --salad-light: #8cc652;
    --hair: #3b2722;
    --jacket: #e9dcb6;
  }
  html, body {
    margin: 0;
    width: 1178px;
    height: 1200px;
    overflow: hidden;
    background: var(--page-bg);
  }
  .book-cover {
    position: absolute;
    left: 256px;
    top: 102px;
    width: 667px;
    height: 995px;
    background: var(--cover-bg);
    overflow: hidden;
  }
  .plate {
    position: absolute;
    left: 16px;
    top: -196px;
    width: 638px;
    height: 638px;
    border-radius: 50%;
    background: var(--plate-rim);
    box-shadow: 0 2px 6px rgba(0,0,0,0.08);
  }
  .plate-salad {
    position: absolute;
    left: 108px;
    top: 60px;
    width: 420px;
    height: 420px;
    border-radius: 50%;
    background: radial-gradient(circle at 50% 45%, var(--salad-light) 0%, var(--salad-green) 70%, #5b9f3a 100%);
  }
  .subtitle-arc {
    position: absolute;
    left: 0;
    top: 0;
    width: 667px;
    height: 460px;
  }
  .subtitle-arc text {
    font-family: 'Oswald', sans-serif;
    font-weight: 600;
    font-size: 32px;
    fill: var(--subtitle);
  }
  .author-photo {
    position: absolute;
    left: 0;
    top: 458px;
    width: 300px;
    height: 448px;
    border-radius: 140px 150px 0 0;
    background: linear-gradient(180deg, var(--hair) 0%, #4a3028 45%, #d9bca4 58%, var(--jacket) 72%, #efe3c2 100%);
  }
  .book-title {
    position: absolute;
    left: 314px;
    top: 506px;
    margin: 0;
    font-family: 'Oswald', sans-serif;
    font-weight: 600;
    font-size: 76px;
    line-height: 74px;
    color: var(--title);
  }
  .book-title span { display: block; }
  .author-band {
    position: absolute;
    left: 0;
    bottom: 0;
    width: 100%;
    height: 89px;
    background: var(--band);
    display: flex;
    align-items: center;
    justify-content: center;
  }
  .author-name {
    font-family: 'Oswald', sans-serif;
    font-weight: 600;
    font-size: 40px;
    color: var(--author-text);
    margin: 0;
  }
</style>
</head>
<body>
  <div class="book-cover">
    <div class="plate">
      <div class="plate-salad" role="img" aria-label="Top-down photo of a Greek salad with greens, cherry tomatoes and feta"></div>
    </div>
    <svg class="subtitle-arc" viewBox="0 0 667 460" aria-label="Reshape Your Habits Around Meals in Only 30 Days">
      <defs>
        <path id="subtitle-path" d="M 46 160 A 292 292 0 0 0 624 160" fill="none"/>
      </defs>
      <text><textPath href="#subtitle-path" startOffset="50%" text-anchor="middle">Reshape Your Habits Around Meals in Only 30 Days</textPath></text>
    </svg>
    <div class="author-photo" role="img" aria-label="Portrait photo of the author in a cream jacket"></div>
    <h1 class="book-title">
      <span>The</span>
      <span>Quiet</span>
      <span>Pantry</span>
      <span>Method</span>
    </h1>
    <div class="author-band">
      <p class="author-name">Marla Voskin</p>
    </div>
  </div>
</body>
</html>
```